Business is called "Pelton Ledger". Accounting and tax services.

I need a flyer for my new business "Pelton Ledger". I am an individual accountant working for himself on the Sunshine Coast in Queensland Australia. I would like to see designs that communicate reliability and trust. I believe my point of difference is that I am always available to my clients and I will cap my number of clients to ensure I can service them properly. Accountants in general seem to have a bad reputation for not responding to clients in a timely fashion, whether by email or phone. This is where I intend to differentiate myself. I have included my business card for ideas on colour and for contact information. I have also included some logo's that should go on the flyer. With the QLA logo, the words "Pelton Ledger is a QLA Business" needs to be written either above, below or to the right hand side (as per the business card).

Target Market(s)

Small business owners and individuals requiring taxation and financials

Industry/Entity Type

Public Accounting

Font styles to use
Serif

Requirements
Must have
• Supplied logo's, accounting style pictures etc
Services: Small Business Taxation
Company & Trust Tax Returns
Rental Property Returns
Capital Gains Tax
Individual Tax Returns
BAS and IAS lodgements
Nice to have
• Needs to convey a sense of being reliable and responds to clients quickly.
Should not have
• My name

```html
<!DOCTYPE html>
<html lang="en">
<head>
<meta charset="utf-8">
<title>Pelton Ledger – Tax &amp; Business Services Flyer</title>
<link rel="stylesheet" href="https://fonts.googleapis.com/css2?family=Roboto+Condensed:wght@700&family=Roboto:wght@400&display=swap">
<style>
  :root {
    --teal: #27b593;
    --black: #000000;
    --white: #ffffff;
    --backdrop: #3d3d3d;
    --display: "Roboto Condensed", "Arial Narrow", sans-serif;
    --body: "Roboto", Arial, sans-serif;
  }
  * { margin: 0; padding: 0; box-sizing: border-box; }
  html, body { width: 1200px; height: 1200px; overflow: hidden; background: var(--backdrop); }
  ul { list-style: none; }
  .flyer {
    position: absolute; left: 172px; top: 0;
    width: 856px; height: 1200px; overflow: hidden;
    background: var(--white);
  }
  .flyer-shapes { position: absolute; inset: 0; }
  .abs { position: absolute; white-space: nowrap; }

  .brand-mark {
    left: 106px; top: 33px; width: 88px; height: 88px;
    border: 3px solid var(--white); border-radius: 50%;
  }
  .brand-name {
    left: 0; width: 300px; top: 136px; text-align: center;
    font: 400 25px/1 var(--body); letter-spacing: 5px; color: var(--white);
  }

  .headline { font: 700 112px/1 var(--display); color: var(--teal); left: 31px; }

  .cta { font: 700 60px/1 var(--display); color: var(--white); left: 46px; }

  .section-title { font: 700 32px/1 var(--display); color: var(--white); }
  .section-rule { height: 3px; background: var(--white); }

  .list-item { font: 400 22px/1 var(--body); color: var(--white); }
  .bullet { width: 6px; height: 6px; border-radius: 50%; background: var(--white); }
  .tick { width: 13px; height: 13px; }

  .footer {
    position: absolute; left: 0; top: 1112px; width: 856px; height: 88px;
    display: flex; align-items: center; gap: 18px;
    padding: 0 30px 0 34px;
    font: 400 17px/1 var(--body); color: var(--white);
  }
  .footer-contact { display: flex; align-items: center; gap: 6px; }
  .footer-contact svg { width: 20px; height: 20px; }
  .qla-name { font: 400 22px/1 var(--body); color: var(--white); margin-left: 6px; }
  .qla-note { font: 400 14px/1.05 var(--body); }
  .agent-badge { width: 38px; height: 48px; background: var(--white); }
  .partner-name { font: 400 17px/1 var(--body); color: var(--white); margin-left: auto; }
</style>
</head>
<body>
<main class="flyer">
  <svg class="flyer-shapes" width="856" height="1200" viewBox="0 0 856 1200" aria-hidden="true">
    <defs>
      <linearGradient id="deskTones" x1="0" y1="0" x2="1" y2="1">
        <stop offset="0" stop-color="#d9b995"/>
        <stop offset="0.45" stop-color="#e9e2d8"/>
        <stop offset="1" stop-color="#6f6a66"/>
      </linearGradient>
      <linearGradient id="coinTones" x1="0" y1="0" x2="0" y2="1">
        <stop offset="0" stop-color="#b9b9b6"/>
        <stop offset="0.55" stop-color="#a0775a"/>
        <stop offset="1" stop-color="#3e3a3a"/>
      </linearGradient>
    </defs>
    <polygon class="band-top" points="0,0 637,0 0,316" fill="var(--teal)"/>
    <polygon class="band-lower" points="0,870 856,453 856,1112 0,1112" fill="var(--teal)"/>
    <polygon class="cta-band" points="23,657 446,657 366,837 0,837 0,703" fill="var(--black)"/>
    <circle cx="613" cy="245" r="252" fill="var(--black)"/>
    <circle cx="613" cy="245" r="247" fill="url(#deskTones)" role="img" aria-label="Photo: accountant working with a calculator, papers and glasses on a desk"/>
    <circle cx="690" cy="554" r="176" fill="var(--white)"/>
    <circle cx="690" cy="554" r="170" fill="url(#coinTones)" role="img" aria-label="Photo: wooden letter blocks spelling TAX on stacks of coins"/>
    <rect x="0" y="1112" width="856" height="88" fill="var(--black)"/>
  </svg>

  <div class="abs brand-mark" aria-hidden="true"></div>
  <div class="abs brand-name">PELTON LEDGER</div>

  <h1>
    <span class="abs headline" style="top:328px">Tax &amp;</span>
    <span class="abs headline" style="top:428px">Business</span>
    <span class="abs headline" style="top:526px">Services</span>
  </h1>

  <div class="abs cta" style="top:674px">Call us Today!</div>
  <div class="abs cta" style="top:749px">0400 555 218</div>

  <h2 class="abs section-title" style="left:36px;top:867px">The Pelton Ledger Difference</h2>
  <div class="abs section-rule" style="left:36px;top:906px;width:116px"></div>
  <ul class="difference-list">
    <li><span class="abs bullet" style="left:41px;top:928px"></span><span class="abs list-item" style="left:57px;top:920px">Prompt reply to all client queries</span></li>
    <li><span class="abs bullet" style="left:41px;top:960px"></span><span class="abs list-item" style="left:57px;top:952px">Reliable &amp; Trustworthy</span></li>
    <li><span class="abs bullet" style="left:41px;top:991px"></span><span class="abs list-item" style="left:57px;top:983px">Personal service</span></li>
    <li><span class="abs bullet" style="left:41px;top:1023px"></span><span class="abs list-item" style="left:57px;top:1015px">You will deal with the same</span><span class="abs list-item" style="left:57px;top:1036px">Accountant from start to finish</span></li>
    <li><span class="abs bullet" style="left:41px;top:1075px"></span><span class="abs list-item" style="left:57px;top:1067px">Lower overheads mean lower prices</span></li>
  </ul>

  <h2 class="abs section-title" style="left:477px;top:771px">Specialising in</h2>
  <div class="abs section-rule" style="left:477px;top:810px;width:115px"></div>
  <ul class="services-list">
    <li>
      <svg class="abs tick" style="left:486px;top:839px" viewBox="0 0 16 16"><circle cx="8" cy="8" r="7" fill="none" stroke="#fff" stroke-width="1.2"/><path d="M4.8 8.2l2.2 2.2 4.2-4.6" fill="none" stroke="#fff" stroke-width="1.3"/></svg>
      <span class="abs list-item" style="left:509px;top:833px">Small Business Taxation</span>
    </li>
    <li>
      <svg class="abs tick" style="left:486px;top:886px" viewBox="0 0 16 16"><circle cx="8" cy="8" r="7" fill="none" stroke="#fff" stroke-width="1.2"/><path d="M4.8 8.2l2.2 2.2 4.2-4.6" fill="none" stroke="#fff" stroke-width="1.3"/></svg>
      <span class="abs list-item" style="left:509px;top:880px">Company &amp; Trust Tax Returns</span>
    </li>
    <li>
      <svg class="abs tick" style="left:486px;top:933px" viewBox="0 0 16 16"><circle cx="8" cy="8" r="7" fill="none" stroke="#fff" stroke-width="1.2"/><path d="M4.8 8.2l2.2 2.2 4.2-4.6" fill="none" stroke="#fff" stroke-width="1.3"/></svg>
      <span class="abs list-item" style="left:509px;top:927px">Rental Property Returns</span>
    </li>
    <li>
      <svg class="abs tick" style="left:486px;top:980px" viewBox="0 0 16 16"><circle cx="8" cy="8" r="7" fill="none" stroke="#fff" stroke-width="1.2"/><path d="M4.8 8.2l2.2 2.2 4.2-4.6" fill="none" stroke="#fff" stroke-width="1.3"/></svg>
      <span class="abs list-item" style="left:509px;top:974px">Capital Gains Tax</span>
    </li>
    <li>
      <svg class="abs tick" style="left:486px;top:1027px" viewBox="0 0 16 16"><circle cx="8" cy="8" r="7" fill="none" stroke="#fff" stroke-width="1.2"/><path d="M4.8 8.2l2.2 2.2 4.2-4.6" fill="none" stroke="#fff" stroke-width="1.3"/></svg>
      <span class="abs list-item" style="left:509px;top:1021px">Individual Tax Returns</span>
    </li>
    <li>
      <svg class="abs tick" style="left:486px;top:1075px" viewBox="0 0 16 16"><circle cx="8" cy="8" r="7" fill="none" stroke="#fff" stroke-width="1.2"/><path d="M4.8 8.2l2.2 2.2 4.2-4.6" fill="none" stroke="#fff" stroke-width="1.3"/></svg>
      <span class="abs list-item" style="left:509px;top:1069px">BAS and IAS lodgements</span>
    </li>
  </ul>

  <footer class="footer">
    <div class="footer-contact">
      <svg viewBox="0 0 20 20"><rect x="1" y="4" width="18" height="12" fill="#fff"/><path d="M1 4l9 7 9-7" fill="none" stroke="#000" stroke-width="1.4"/></svg>
      <span>hi@peltonledger.com.au</span>
    </div>
    <div class="footer-contact">
      <svg viewBox="0 0 20 20"><circle cx="10" cy="10" r="8.5" fill="none" stroke="#fff" stroke-width="1.6"/><ellipse cx="10" cy="10" rx="3.6" ry="8.5" fill="none" stroke="#fff" stroke-width="1.3"/><path d="M1.5 10h17" stroke="#fff" stroke-width="1.3"/></svg>
      <span>www.peltonledger.com.au</span>
    </div>
    <span class="qla-name">QLA</span>
    <div class="qla-note">Pelton Ledger is a<br>QLA Business</div>
    <div class="agent-badge" role="img" aria-label="Registered tax agent badge"></div>
    <span class="partner-name">Ledgerly</span>
  </footer>
</main>
</body>
</html>
```